B2B EDM Banner Design- Specialist Tech Company

We need a new top-of-email banner for our EDM campaigns for Varnel Brix (www.varnelbrix-example.com
). This banner will sit at the top of every email and must immediately signal the brand, look modern and professional, and be visually aligned with the tech/IT audience.
Size of the banner: Around 728x90 - it must fit at the top of an email blast.
Purpose of the Banner
Establish a strong, recognizable brand identity across all Varnel Brix EDMs
visually consistent with existing banners created for other brands (see reference examples provided)
Communicate Varnel Brix’s value proposition at a glance
Brand Name
Varnel Brix
Tagline (must appear in the banner)
“11,322 whitepapers from 726 companies”
Design Requirements
Style & Tone
Modern, clean, and professional
Tech-centric look and feel
High-quality, sleek, and corporate
Eye-catching but not cluttered
Should feel premium and authoritative
Layout & Composition
Full-width banner for email header
Horizontal orientation similar to the Plomtar and Quindle Staff Archive examples
Include space for the brand name/logo prominently on the left or centered
Integrate the tagline in a readable, secondary position
Optional: a subtle background texture or tech-related abstract pattern (circuitry, network nodes, gradient, etc.)
No busy imagery—should feel clean and trustworthy
Color Palette
Use colors consistent with Varnel Brix branding from www.varnelbrix-example.com
Blues, greys, blacks, and tech-style gradients preferred
Should feel consistent with a B2B IT audience
Typography
Clean, sans-serif fonts (professional/tech-aligned)
Brand name should be bold and prominent
Tagline should be smaller, but still readable on desktop and mobile
Imagery (if used)
Abstract tech shapes, network visuals, geometric patterns, or gradient overlays
Avoid photography of people
Keep imagery subtle so text remains legible
Call-to-Action Button (optional)
None required in this banner (unlike the HR examples)
Banner should remain a pure brand header
Deliverables
Final banner in PNG and JPG formats
2–3 design variations (if possible) for A/B testing
Dimensions optimized for EDM: ~600–700px wide (standard email width), proportionate height

```html
<!DOCTYPE html>
<html lang="en">
<head>
<meta charset="utf-8">
<title>Varnel Brix – Email Header Banner</title>
<link rel="stylesheet" href="https://fonts.googleapis.com/css2?family=Montserrat:wght@600;700&family=Open+Sans:wght@400;700&display=swap">
<style>
  :root {
    --page-bg: #f2f2f0;
    --navy-deep: #23214f;
    --navy: #2b3378;
    --blue-mid: #2f5bb0;
    --blue-bright: #2aa3dc;
    --trace-blue: #3fa6e6;
    --text-light: #ffffff;
    --text-soft: #e4eefa;
    --mark-blue: #3b8fe0;
  }

  * { box-sizing: border-box; margin: 0; padding: 0; }

  html, body {
    width: 1200px;
    height: 926px;
    overflow: hidden;
    background: var(--page-bg);
  }

  .canvas {
    position: relative;
    width: 1200px;
    height: 926px;
    display: flex;
    align-items: center;
    justify-content: center;
  }

  .email-banner {
    position: relative;
    width: 1100px;
    height: 136px;
    overflow: hidden;
    background: linear-gradient(90deg,
      var(--navy-deep) 0%,
      var(--navy-deep) 40%,
      var(--navy) 58%,
      var(--blue-mid) 78%,
      var(--blue-bright) 100%);
  }

  .tech-pattern {
    position: absolute;
    left: 0;
    top: 0;
    width: 62%;
    height: 100%;
    background:
      radial-gradient(ellipse at 40% 20%, rgba(63, 166, 230, 0.18), transparent 55%),
      linear-gradient(90deg, rgba(63, 166, 230, 0.14), rgba(63, 166, 230, 0) 100%);
  }

  .network-glow {
    position: absolute;
    right: 0;
    top: 0;
    width: 30%;
    height: 100%;
    background: radial-gradient(ellipse at 80% 20%, rgba(255, 255, 255, 0.16), transparent 60%);
  }

  .brand-block {
    position: absolute;
    right: 70px;
    top: 50%;
    transform: translateY(-50%);
    display: flex;
    align-items: center;
    gap: 22px;
  }

  .brand-dot {
    width: 58px;
    height: 58px;
    border-radius: 50%;
    background: var(--mark-blue);
    flex: none;
  }

  .brand-text {
    display: flex;
    flex-direction: column;
  }

  .brand-name {
    font-family: "Montserrat", sans-serif;
    font-weight: 700;
    font-size: 44px;
    line-height: 1;
    letter-spacing: 0.5px;
    color: var(--text-light);
    text-transform: uppercase;
  }

  .brand-audience {
    margin-top: 6px;
    font-family: "Open Sans", sans-serif;
    font-weight: 400;
    font-size: 13px;
    letter-spacing: 9.5px;
    color: var(--text-soft);
    text-transform: uppercase;
  }

  .brand-tagline {
    margin-top: 6px;
    font-family: "Open Sans", sans-serif;
    font-weight: 400;
    font-size: 17px;
    color: var(--text-soft);
  }

  .brand-tagline strong {
    font-weight: 700;
    color: var(--text-light);
  }
</style>
</head>
<body>
  <main class="canvas">
    <header class="email-banner">
      <div class="tech-pattern" role="img" aria-label="Abstract circuit board traces with glowing nodes"></div>
      <div class="network-glow" role="img" aria-label="Faint network line pattern"></div>

      <div class="brand-block">
        <span class="brand-dot" aria-hidden="true"></span>
        <div class="brand-text">
          <h1 class="brand-name">Varnel Brix</h1>
          <p class="brand-audience">For IT Professionals</p>
          <p class="brand-tagline"><strong>11,322</strong> whitepapers from <strong>726</strong> companies</p>
        </div>
      </div>
    </header>
  </main>
</body>
</html>
```